Velvet Evening Soirée Flyer for a female oriented event

I need a flyer to promote my event which should look "FUN" and "Sophisticated"
I would need the flyer to be 8 1/2" X 11" 300 dpi. I would need the layered .psd file as well as all the fonts. The flyer should contain the following info:

Velvet Evening Soirée CT
Friday, September 25th
6:00-10:00 PM
The Jasper Hall Pavilion
7 Orwell Ln
Danbury, CT 06811
First 100 guests will have a chance to win $25,000 and receive a swag bag filled with gifts
$20 Advanced Admission at www.velveteveningsoireect.example
$25 at the door
(Key words)
Martini Bar
Wine Tasting
Food Sampling
Beauty Make-Overs
Fashion Shows
Psychic Readings
Shopping
Door Prizes
Swag Bag
Exhibitors
For tickets visit www.velveteveningsoireect.example

Target Market(s)

Ladies

Industry/Entity Type

Event

Requirements
Must have
• see description

```html
<!DOCTYPE html>
<html lang="en">
<head>
<meta charset="utf-8">
<title>Velvet Evening Soirée CT — Flyer</title>
<link rel="stylesheet" href="https://fonts.googleapis.com/css2?family=Pinyon+Script&family=Questrial&display=swap">
<style>
  :root {
    --backdrop: #e9e7ec;
    --paper: #ffffff;
    --night: #000000;
    --sky-top: #2e3a47;
    --sky-mid: #6b6a68;
    --sky-warm: #c4763a;
    --sky-glow: #e06a18;
    --yellow: #f3d24a;
    --orange: #f08a3c;
    --cyan: #35b6e6;
    --lime: #b9d64a;
    --rule: #6a6a6a;
  }
  * { box-sizing: border-box; margin: 0; padding: 0; }
  html, body { width: 969px; height: 1200px; overflow: hidden; background: var(--backdrop); }
  .flyer {
    position: absolute; left: 80px; top: 38px;
    width: 809px; height: 1124px;
    background: var(--paper); padding: 16px;
    box-shadow: 0 6px 18px rgba(0,0,0,.18);
  }
  .flyer__inner {
    position: relative; width: 777px; height: 1092px;
    background: var(--night); overflow: hidden;
    font-family: "Questrial", "Century Gothic", sans-serif;
  }
  .hero {
    position: absolute; left: 0; top: 0; width: 777px; height: 640px;
    background: linear-gradient(180deg, var(--sky-top) 0%, var(--sky-mid) 40%, var(--sky-warm) 65%, var(--sky-glow) 82%, var(--night) 100%);
  }
  .title { position: absolute; left: 0; top: 0; color: var(--night); font-family: "Pinyon Script", "Snell Roundhand", cursive; font-weight: 400; }
  .title__main { position: absolute; left: 18px; top: 285px; font-size: 210px; line-height: 1; white-space: nowrap; }
  .title__sub { position: absolute; left: 190px; top: 455px; font-size: 60px; line-height: 1; white-space: nowrap; }
  .details {
    position: absolute; left: 105px; top: 675px; width: 567px;
    text-align: center;
  }
  .details__row { padding: 11px 0; border-bottom: 1px dashed var(--rule); font-size: 19px; line-height: 1.2; }
  .details__date { color: var(--yellow); }
  .details__venue { color: var(--orange); text-transform: uppercase; font-size: 18px; letter-spacing: .3px; }
  .details__prize { color: var(--cyan); }
  .details__prize strong { font-weight: 700; }
  .details__price { color: var(--lime); }
  .keywords {
    position: absolute; left: 0; top: 918px; width: 777px;
    text-align: center; color: var(--orange);
    font-size: 14px; font-weight: 700; line-height: 19px; text-transform: uppercase; letter-spacing: .3px;
  }
  .cta {
    position: absolute; left: 0; top: 995px; width: 777px;
    text-align: center; color: var(--cyan); font-size: 26px; font-weight: 700;
  }
</style>
</head>
<body>
  <div class="flyer">
    <div class="flyer__inner">
      <div class="hero" role="img" aria-label="Photograph: silhouette of a woman leaping with a flowing scarf against a sunset sky over a grassy horizon"></div>
      <h1 class="title">
        <span class="title__main">Velvet</span>
        <span class="title__sub">evening soirée ct</span>
      </h1>
      <div class="details">
        <p class="details__row details__date">Friday, September 25th 6:00-10:00 PM</p>
        <p class="details__row details__venue">The Jasper Hall Pavilion 7 Orwell Ln, Danbury, CT 06811</p>
        <p class="details__row details__prize">First 100 guests will have a chance to win <strong>$25,000</strong> and receive<br>a swag bag filled with gifts</p>
        <p class="details__row details__price">$20 Advanced Admission at www.velveteveningsoireect.example<br>$25 at the door</p>
      </div>
      <p class="keywords">
        Martini Bar | Wine Tasting | Food Sampling<br>
        Beauty Make-Overs | Fashion Shows | Psychic Readings<br>
        Shopping | Door Prizes | Swag Bag | Exhibitors
      </p>
      <p class="cta">For tickets visit www.velveteveningsoireect.example</p>
    </div>
  </div>
</body>
</html>
```